Market Intelligence Modules

Take the existing power point and add graphics to each slide and use photos and graphics to create a power point presentation that has the look and feel of a high tech company / research - with a theme of commercial real estate. To learn more about what the company does you can go to www.kovanstel.com.

Target Market(s)

Target market are financial institutions and commercial real estate developers - going for high tech research look and feel and showing commercial real estate. ONLY commercial real estate.

Industry/Entity Type

Real Estate

Requirements
Must have
• Must have Brindlequay logo and must communicate that Brindlequay can process large amounts of data and analytics. Each slide should have some type of image that represents data or commercial real estate.
Should not have
• No blank white slides.

```html
<!DOCTYPE html>
<html lang="en">
<head>
<meta charset="utf-8">
<title>Brindlequay – Market Intelligence Modules</title>
<link href="https://fonts.googleapis.com/css2?family=Lato:wght@300;400;700&display=swap" rel="stylesheet">
<style>
:root{
  --canvas:#dcdde0;
  --header:#3a3b41;
  --title-blue:#2f6cf5;
  --brand-green:#3fc33a;
  --royal:#2b57f0;
  --deep-blue:#1a5fb0;
  --navy:#2a2e3a;
  --slide-grey:#c9ccd1;
  --text-dark:#4a4d55;
  --caption-blue:#4a86c8;
  --orange:#e07a2e;
  --table-yellow:#f2ee3a;
}
*{box-sizing:border-box;margin:0;padding:0}
html,body{width:1200px;height:899px;overflow:hidden;background:var(--canvas);font-family:'Lato',sans-serif}
.board{position:relative;width:1200px;height:899px}
.slide{position:absolute;width:357px;height:276px;overflow:hidden;background:linear-gradient(160deg,#e4e6e9,#c2c6cc)}
.slide-header{height:33px;background:var(--header);color:var(--title-blue);font-weight:300;font-size:14px;line-height:33px;padding-left:15px;letter-spacing:.2px}
.slide-footer{position:absolute;left:0;right:0;bottom:0;height:4px;background:var(--header)}
.slide-footer::after{content:"";position:absolute;right:0;bottom:0;width:100px;height:6px;background:var(--brand-green);clip-path:polygon(8% 0,100% 0,100% 100%,0 100%)}
.page-num{position:absolute;right:10px;bottom:0;font-size:4px;color:#fff;z-index:2}
.brand{position:absolute;color:var(--brand-green);font-weight:400;letter-spacing:-.3px}
.brand-sm{left:11px;bottom:9px;font-size:11px}
.photo{position:absolute}
.col{position:absolute}
.r1{top:21px}.r2{top:308px}.r3{top:603px}
.c1{left:52px}.c2{left:424px}.c3{left:790px}

.title-slide{background:linear-gradient(180deg,#2c2d32,#3d3e44)}
.title-band{left:0;top:67px;width:357px;height:103px;background:linear-gradient(110deg,#3550f2,#2b4fe8 60%,#4a6cf7)}
.title-slide .stripe{position:absolute;background:var(--brand-green)}
.title-text{position:absolute;left:26px;top:125px;color:#fff;font-weight:300;font-size:14.5px}
.title-sub{position:absolute;left:29px;top:148px;color:#c9d3ff;font-size:7px;font-weight:300}
.brand-lg{right:20px;bottom:26px;font-size:22px}

.z-band{position:absolute;left:0;top:59px;width:357px;height:76px;background:#8a8d92;opacity:.85}
.z-map{left:13px;top:51px;width:122px;height:91px;background:radial-gradient(circle at 50% 50%,#1a6fe0,#06122a 70%)}
.z-q{position:absolute;left:157px;top:91px;color:#fff;font-size:14px;font-weight:300}
.z-list{position:absolute;left:156px;top:158px;width:190px;list-style:none;font-size:7px;color:var(--text-dark);line-height:1.35}
.z-list li{margin-bottom:8px;padding-left:5px;position:relative}
.z-list li::before{content:"•";position:absolute;left:0;color:#2f6cf5}

.rw-img{left:18px;top:46px;width:327px;height:83px;background:linear-gradient(100deg,#1b2a8a,#2bb0e6 45%,#9fe3f6 60%,#2a78c9)}
.rw-list{position:absolute;top:161px;list-style:none;font-size:9px;color:var(--text-dark);font-weight:400;line-height:18.5px}
.rw-list li::before{content:"•";color:#2f6cf5;margin-right:7px}

.obj-body{position:absolute;left:0;top:33px;width:357px;height:239px;background:linear-gradient(180deg,#fff,#eef0f3)}
.obj-photo{left:25px;top:85px;width:128px;height:72px;background:radial-gradient(ellipse at 55% 50%,#3b6fe6,#1a3a9c 50%,#f4f5f7 78%)}
.obj-caption{position:absolute;left:24px;top:160px;width:130px;text-align:center;color:var(--caption-blue);font-size:9.5px;line-height:12.5px;font-weight:300}
.bubble{position:absolute;width:48px;height:48px;border-radius:50%;border:3px solid #8a8e96;color:#fff;font-size:6px;display:flex;align-items:center;justify-content:center;text-align:center;line-height:1.1}

.dt-wrap{position:absolute;left:62px;top:67px}

.syn-panel{position:absolute;left:19px;top:65px;width:321px;height:163px;background:#fff;box-shadow:0 1px 3px rgba(0,0,0,.25)}

.contact{background:#fff}
.contact-blue{position:absolute;left:0;top:103px;width:357px;height:173px;background:linear-gradient(120deg,#1a63c4,#1e78d6 55%,#0f4f9e)}
.contact-line{position:absolute;top:98px;height:4px}
.contact-info{position:absolute;left:24px;top:136px;color:#d8e6fa;font-size:5.6px;line-height:7.6px;font-weight:300}
.contact-info p{margin-bottom:6px}
.social{display:flex;gap:3px;margin-top:3px}
.social span{width:8px;height:8px;background:#fff;border-radius:1px}
.ico{display:inline-block;width:6px;height:6px;border-radius:50%;background:#fff;vertical-align:-1px;margin-right:3px}
</style>
</head>
<body>
<div class="board">

  <section class="slide title-slide r1 c1">
    <div class="photo title-band" role="img" aria-label="Blue-tinted photo of a glass office tower facade"></div>
    <span class="stripe" style="left:250px;top:60px;width:107px;height:8px;clip-path:polygon(8% 0,100% 0,100% 100%,0 100%)"></span>
    <span class="stripe" style="left:195px;top:168px;width:40px;height:26px;clip-path:polygon(70% 0,100% 0,30% 100%,0 100%)"></span>
    <p class="title-text">Lorem ipsum dolor sit amet</p>
    <p class="title-sub">Birmingham, March 25, 2013</p>
    <span class="brand brand-lg">Brindlequay</span>
  </section>

  <section class="slide r1 c2">
    <header class="slide-header">ZETTABYTE</header>
    <div class="z-band"></div>
    <div class="photo z-map" role="img" aria-label="Blue world map over a field of binary digits"></div>
    <p class="z-q">What is a zettabyte?</p>
    <ul class="z-list">
      <li>One zettabyte of data allows you to stack books from Earth to Pluto 20 times (72 billion miles)</li>
      <li>If one gigabyte of data were a cup of coffee a zettabyte would equal the Great Wall of China</li>
      <li>In 2015 all internet traffic will exceed one zettabyte of data - 540,000 time increase from 2003</li>
    </ul>
    <span class="brand brand-sm">Brindlequay</span>
    <div class="slide-footer"></div><span class="page-num">2</span>
  </section>

  <section class="slide r1 c3">
    <header class="slide-header">REAL WORLD DATA ENVIRONMENT</header>
    <div class="photo rw-img" role="img" aria-label="Glowing blue network of connected people icons"></div>
    <ul class="rw-list" style="left:80px"><li>Overload</li><li>Unorganized</li><li>Disperse</li><li>Quantitative</li></ul>
    <ul class="rw-list" style="left:198px"><li>Qualitative</li><li>Relevance</li><li>Trends</li><li>Timeliness</li></ul>
    <span class="brand brand-sm">Brindlequay</span>
    <div class="slide-footer"></div><span class="page-num">2</span>
  </section>

  <section class="slide r2 c1">
    <header class="slide-header">REPORT OBJECTIVES</header>
    <div class="obj-body"></div>
    <div class="photo obj-photo" role="img" aria-label="Cluster of blue marbles with a single red marble"></div>
    <p class="obj-caption">Consolidating information in formats that are under-standable, meaningful and actionable</p>
    <div class="bubble" style="left:235px;top:50px;background:#9b6a6a">Trending</div>
    <div class="bubble" style="left:176px;top:111px;background:#a57a5e">Relevance</div>
    <div class="bubble" style="left:240px;top:116px;width:38px;height:38px;background:#c4a584;font-size:5.5px">Indexes Report</div>
    <div class="bubble" style="left:295px;top:111px;background:#5b6b9e;font-size:5.5px">Consilidated</div>
    <div class="bubble" style="left:235px;top:170px;background:#6e9a6a">Timeliness</div>
    <span class="brand brand-sm">Brindlequay</span>
    <div class="slide-footer"></div><span class="page-num">2</span>
  </section>

  <section class="slide r2 c2" style="left:418px">
    <header class="slide-header">THE INTERPRETATION PROCESS</header>
    <svg class="col" style="left:30px;top:93px" width="298" height="59" viewBox="0 0 315 62" font-family="Lato, sans-serif" font-size="6" font-weight="700" fill="#fff" text-anchor="middle">
      <polygon points="8,0 66,0 82,31 66,62 8,62 22,31" fill="#1b6fb8"/>
      <polygon points="70,0 130,0 146,31 130,62 70,62 84,31" fill="#2a2e3a"/>
      <polygon points="134,0 194,0 210,31 194,62 134,62 148,31" fill="#1b6fb8"/>
      <polygon points="198,0 254,0 270,31 254,62 198,62 212,31" fill="#2a2e3a"/>
      <polygon points="258,0 300,0 315,31 300,62 258,62 272,31" fill="#1b6fb8"/>
      <text x="44" y="29">Database</text><text x="44" y="37">Integration</text>
      <text x="107" y="29">Quantitatve</text><text x="107" y="37">Research</text>
      <text x="171" y="30">Qualitatve</text><text x="171" y="38">Research</text>
      <text x="233" y="29">Indexes</text><text x="233" y="37">Reports</text>
      <text x="289" y="21">Times</text><text x="289" y="28">Staped</text><text x="289" y="35">Market</text><text x="289" y="42">Updates</text>
    </svg>
    <span class="brand brand-sm">Brindlequay</span>
    <div class="slide-footer"></div><span class="page-num">2</span>
  </section>

  <section class="slide r2 c3">
    <header class="slide-header">DATA REPORTING RESOURCES</header>
    <svg class="dt-wrap" width="208" height="166" viewBox="0 0 208 166">
      <rect width="208" height="166" fill="#fff" opacity=".55" stroke="#333" stroke-width=".6"/>
      <rect x="0" y="10" width="208" height="5" fill="var(--table-yellow)"/>
      <rect x="0" y="57" width="208" height="5" fill="var(--table-yellow)"/>
      <rect x="0" y="93" width="208" height="10" fill="var(--table-yellow)"/>
      <rect x="0" y="118" width="208" height="5" fill="var(--table-yellow)"/>
      <g stroke="#333" stroke-width=".4">
        <line x1="20" y1="0" x2="20" y2="166"/><line x1="38" y1="0" x2="38" y2="166"/><line x1="56" y1="0" x2="56" y2="166"/>
        <line x1="72" y1="0" x2="72" y2="166"/><line x1="88" y1="0" x2="88" y2="166"/><line x1="104" y1="0" x2="104" y2="166"/>
        <line x1="120" y1="0" x2="120" y2="166"/><line x1="136" y1="0" x2="136" y2="166"/><line x1="152" y1="0" x2="152" y2="166"/>
        <line x1="168" y1="0" x2="168" y2="166"/><line x1="184" y1="0" x2="184" y2="166"/>
        <line x1="0" y1="10" x2="208" y2="10"/><line x1="0" y1="22" x2="208" y2="22"/><line x1="0" y1="34" x2="208" y2="34"/>
        <line x1="0" y1="46" x2="208" y2="46"/><line x1="0" y1="57" x2="208" y2="57"/><line x1="0" y1="70" x2="208" y2="70"/>
        <line x1="0" y1="82" x2="208" y2="82"/><line x1="0" y1="93" x2="208" y2="93"/><line x1="0" y1="108" x2="208" y2="108"/>
        <line x1="0" y1="118" x2="208" y2="118"/><line x1="0" y1="130" x2="208" y2="130"/><line x1="0" y1="142" x2="208" y2="142"/>
        <line x1="0" y1="154" x2="208" y2="154"/>
      </g>
    </svg>
    <span class="brand brand-sm" style="font-size:8px">Brindlequay</span>
    <div class="slide-footer"></div><span class="page-num">2</span>
  </section>

  <section class="slide r3 c1">
    <header class="slide-header">REPORT OBJECTIVES</header>
    <svg class="col" style="left:23px;top:43px" width="280" height="210" viewBox="0 0 280 210">
      <rect width="280" height="7" fill="var(--orange)"/>
      <rect y="7" width="280" height="95" fill="#fff" opacity=".6"/>
      <rect y="9" width="60" height="93" fill="var(--orange)" opacity=".18"/>
      <g stroke="var(--orange)" stroke-width=".5" opacity=".7">
        <line x1="0" y1="14" x2="280" y2="14"/><line x1="0" y1="28" x2="280" y2="28"/><line x1="0" y1="42" x2="280" y2="42"/>
        <line x1="0" y1="56" x2="280" y2="56"/><line x1="0" y1="70" x2="280" y2="70"/><line x1="0" y1="84" x2="280" y2="84"/>
      </g>
      <g stroke="#999" stroke-width=".3">
        <line x1="0" y1="21" x2="280" y2="21"/><line x1="0" y1="35" x2="280" y2="35"/><line x1="0" y1="49" x2="280" y2="49"/>
        <line x1="0" y1="63" x2="280" y2="63"/><line x1="0" y1="77" x2="280" y2="77"/><line x1="0" y1="91" x2="280" y2="91"/>
      </g>
      <g fill="var(--orange)">
        <rect x="68" y="112" width="2" height="92"/><rect x="226" y="112" width="2" height="92"/>
        <rect x="70" y="116" width="26" height="2"/><rect x="70" y="128" width="14" height="2"/><rect x="70" y="140" width="10" height="2"/>
        <rect x="64" y="152" width="4" height="2"/><rect x="70" y="164" width="6" height="2"/><rect x="58" y="176" width="10" height="2"/>
        <rect x="70" y="188" width="4" height="2"/><rect x="40" y="200" width="28" height="2"/>
        <rect x="228" y="114" width="30" height="2"/><rect x="228" y="126" width="16" height="2"/><rect x="228" y="138" width="8" height="2"/>
        <rect x="220" y="150" width="6" height="2"/><rect x="228" y="162" width="4" height="2"/><rect x="212" y="174" width="14" height="2"/>
        <rect x="218" y="186" width="8" height="2"/><rect x="192" y="200" width="34" height="2"/>
      </g>
    </svg>
    <span class="brand brand-sm" style="font-size:8px">Brindlequay</span>
    <div class="slide-footer"></div><span class="page-num">2</span>
  </section>

  <section class="slide r3 c2" style="left:420px">
    <header class="slide-header">SOURCE SYNOPSIS</header>
    <div class="syn-panel">
      <svg width="321" height="163" viewBox="0 0 321 163">
        <g fill="#b8bcc4">
          <circle cx="30" cy="28" r="14"/><circle cx="78" cy="28" r="14" fill="#8a7a3a"/><circle cx="136" cy="28" r="14" fill="#9a8a5a"/>
          <circle cx="210" cy="28" r="14" fill="#3a4a8a"/><circle cx="284" cy="28" r="14" fill="#2a4a9a"/>
          <circle cx="30" cy="76" r="14" fill="#b23a2a"/><rect x="58" y="70" width="44" height="10" fill="#5a4a8a"/>
          <rect x="118" y="66" width="44" height="16" fill="#1a4a9a"/><rect x="186" y="70" width="44" height="12" fill="#3a5a9a"/>
          <rect x="262" y="64" width="40" height="14" fill="#2a5aa0"/>
          <rect x="20" y="118" width="50" height="10" fill="#7a7a7a"/><rect x="84" y="112" width="80" height="6" fill="#2a5aa0"/>
          <rect x="178" y="104" width="36" height="20" fill="#c43a2a"/><rect x="226" y="104" width="50" height="20" fill="#2a4a9a"/>
          <rect x="288" y="108" width="22" height="10" fill="#2a4a9a"/>
          <rect x="20" y="148" width="62" height="8" fill="#d08a2a"/><rect x="110" y="136" width="56" height="18" fill="#2a8aa0"/>
          <rect x="182" y="140" width="60" height="12" fill="#9a6a8a"/><rect x="248" y="138" width="36" height="16" fill="#111"/>
          <rect x="290" y="138" width="24" height="16" fill="#3a8a3a"/>
        </g>
      </svg>
    </div>
    <span class="brand brand-sm" style="font-size:8px">Brindlequay</span>
    <div class="slide-footer"></div><span class="page-num">2</span>
  </section>

  <section class="slide contact r3 c3">
    <span class="brand" style="left:24px;top:44px;font-size:22px">Brindlequay</span>
    <div class="photo contact-blue" role="img" aria-label="Blue-toned photo of a curved glass office building"></div>
    <span class="contact-line" style="left:0;width:260px;background:#1e4fe8"></span>
    <span class="contact-line" style="left:258px;width:99px;top:96px;height:6px;background:var(--brand-green);clip-path:polygon(8% 0,100% 0,100% 100%,0 100%)"></span>
    <div class="contact-info">
      <p>Brindlequay – Downtown Chicago<br>218 North Orchard Street<br>Suite 200<br>Lakeview, IL – 60614</p>
      <p>Brindlequay – North / West Suburbs<br>1740 Meadow Ridge Drive<br>Suite 201<br>Elmwood, IL – 60145</p>
      <p><span class="ico"></span>+1.415.555.0148<br><span class="ico"></span>info@kovanstel.com<br><span class="ico"></span>www.kovanstel.com</p>
      <div class="social"><span></span><span></span><span></span></div>
    </div>
  </section>

</div>
</body>
</html>
```